New local Orchid nursery branding

We need a business card designed for our small local company in Darwin, Australia that grows orchids, called Blooms at Carrow.
We will be running private sales from our property, and handing these out at local events for perspective customers.

We would like to see designs that are simple, and able to be used with minimal colours and containing an orchid, preferably a stylised representation instead of a photo.
The eventual hope is to take this into larger formats to create our company logo/branding etc, but for now we just need business cards.

Target Market(s)

Local Orchid

Industry/Entity Type

Business

Contact Information for Business Card

Company Name
Logo
Name
Phone Number
Street Address
Email Address (less prominent than rest of the text)

Font styles to use
Sans Serif

Requirements
Must have
• Name of the company, which is Blooms at Carrow
Nice to have
• stylised orchid logo
Should not have
• too many colours

```html
<!DOCTYPE html>
<html lang="en">
<head>
<meta charset="utf-8">
<title>Blooms at Carrow – Business Card</title>
<link rel="stylesheet" href="https://fonts.googleapis.com/css2?family=Questrial&display=swap">
<style>
  :root {
    --magenta: #b3208e;
    --magenta-deep: #9a1578;
    --pink-light: #eaa3d4;
    --pink-soft: #f4d3ea;
    --card-white: #ffffff;
    --backdrop: #e6e3e6;
  }
  html, body {
    margin: 0;
    padding: 0;
    width: 1200px;
    height: 720px;
    overflow: hidden;
    background: var(--backdrop);
  }
  .canvas {
    position: relative;
    width: 1200px;
    height: 720px;
  }
  .business-card {
    position: absolute;
    left: 75px;
    top: 60px;
    width: 1050px;
    height: 600px;
    box-shadow: 0 10px 30px rgba(0,0,0,0.18);
  }
  .business-card svg { display: block; }
  .brand-name {
    font-family: "Questrial", sans-serif;
    font-size: 50px;
    fill: var(--card-white);
    letter-spacing: 1px;
  }
  .contact-text {
    font-family: "Questrial", sans-serif;
    font-size: 27px;
    fill: var(--magenta);
  }
  .icon { fill: var(--magenta); }
  .icon-line { fill: none; stroke: var(--card-white); stroke-width: 2; }
</style>
</head>
<body>
<main class="canvas">
  <section class="business-card" aria-label="Blooms at Carrow business card">
    <svg width="1050" height="600" viewBox="0 0 1050 600">
      <defs>
        <radialGradient id="orchid-tones" cx="50%" cy="45%" r="55%">
          <stop offset="0%" stop-color="#e7c6e4"/>
          <stop offset="60%" stop-color="#f1dcef"/>
          <stop offset="100%" stop-color="#ffffff" stop-opacity="0"/>
        </radialGradient>
        <linearGradient id="pinwheel-tones" x1="0" y1="0" x2="1" y2="1">
          <stop offset="0%" stop-color="#c23a9f"/>
          <stop offset="100%" stop-color="#a4167f"/>
        </linearGradient>
      </defs>

      <rect class="card-face" width="1050" height="600" fill="var(--card-white)"/>

      <!-- header band -->
      <path class="header-stripe" d="M0,0 H1050 V140 C860,200 700,120 500,178 C310,230 150,178 0,188 Z" fill="var(--pink-light)"/>
      <path class="header-band" d="M0,0 H1050 V126 C860,186 700,106 500,164 C310,216 150,164 0,174 Z" fill="var(--magenta)"/>

      <!-- brand -->
      <circle class="brand-dot" cx="60" cy="78" r="18" fill="var(--card-white)"/>
      <text class="brand-name" x="95" y="95">Blooms at Carrow</text>

      <!-- orchid artwork area -->
      <ellipse role="img" aria-label="Pink orchid spray illustration" cx="740" cy="330" rx="230" ry="170" fill="url(#orchid-tones)"/>

      <!-- footer band -->
      <path class="footer-stripe" d="M0,508 C300,528 620,470 1050,410 V600 H0 Z" fill="var(--pink-light)"/>
      <path class="footer-band" d="M0,522 C300,542 620,484 1050,424 V600 H0 Z" fill="var(--magenta)"/>
      <path role="img" aria-label="Decorative petal pinwheel motif" d="M780,600 C790,520 860,455 1050,424 V600 Z" fill="url(#pinwheel-tones)"/>

      <!-- contact details -->
      <g class="contact-list">
        <g class="contact-address">
          <path class="icon" d="M66,230 a10,10 0 0 1 20,0 c0,8 -10,18 -10,18 c0,0 -10,-10 -10,-18 z"/>
          <circle cx="76" cy="230" r="3.5" fill="var(--card-white)"/>
          <text class="contact-text" x="108" y="246">company address</text>
        </g>
        <g class="contact-phone">
          <path class="icon" d="M68,282 c2,-4 6,-5 8,-3 l3,5 c1,2 0,3 -2,4 c1,4 4,7 8,9 c1,-2 3,-3 4,-2 l5,3 c2,2 1,6 -3,8 c-10,2 -25,-12 -23,-24 z"/>
          <text class="contact-text" x="108" y="304">0123 45 678</text>
        </g>
        <g class="contact-email">
          <rect class="icon" x="64" y="344" width="24" height="17" rx="2"/>
          <path class="icon-line" d="M65,346 L76,355 L87,346"/>
          <text class="contact-text" x="108" y="362">email@Companyname.com</text>
        </g>
        <g class="contact-web">
          <circle class="icon" cx="76" cy="388" r="11"/>
          <path class="icon-line" d="M65,388 H87 M76,377 C70,382 70,394 76,399 M76,377 C82,382 82,394 76,399"/>
          <text class="contact-text" x="108" y="397">www.companyname.com</text>
        </g>
      </g>
    </svg>
  </section>
</main>
</body>
</html>
```